Stationery Required - Own Logo provided

Hi,

We are a retail company called 'Copperfinch Trading Limited' based in the UK and would like some corporate stationery designed.

We have provided our Logo which we would like to use (Its attached to this brief)...

The designs must be orginal, professional, stylish and interesting!

Target Market(s)

We will use this stationery to communicate with our wholesale suppliers and employees, so it must have a 'professional' feel about it.

Industry/Entity Type

It Company

Requirements
Must have
• Must be professional, corporate, stylish and not to 'fussy'. we require ... Business card design, a4 letter, compliment slip. All designs must be supplied in a format where the text (address/telephone numbers etc..) can be edited, as we have alot of staff and operate out of several different premises.
Nice to have
• I would like a windows backround picture file supplied as well so we can integrate that onto our computer systems.

```html
<!DOCTYPE html>
<html lang="en">
<head>
<meta charset="utf-8">
<title>Copperfinch Trading Limited – Stationery</title>
<link href="https://fonts.googleapis.com/css2?family=Fira+Sans:wght@300;400&display=swap" rel="stylesheet">
<style>
  :root {
    --paper: #ffffff;
    --edge: #1a1a1a;
    --forest: #30511f;
    --leaf: #6fb52c;
    --brand: #5fa324;
    --ink-dark: #3d5a1c;
  }
  * { margin: 0; padding: 0; box-sizing: border-box; }
  html, body { width: 1200px; height: 900px; overflow: hidden; background: var(--paper); }
  body { position: relative; font-family: "Fira Sans", Arial, sans-serif; font-weight: 300; }

  .sheet { position: absolute; background: var(--paper); border: 1px solid var(--edge); }
  .sheet--dark { background: var(--forest); border: none; }

  .brand { display: flex; align-items: center; gap: 4px; color: var(--brand); font-weight: 400; white-space: nowrap; }
  .brand__mark { background: var(--brand); flex: none; }

  /* business card */
  .card-front { left: 218px; top: 60px; width: 199px; height: 118px; display: flex; align-items: center; justify-content: center; }
  .card-front .brand { font-size: 8.5px; }
  .card-front .brand__mark { width: 9px; height: 9px; }

  .card-back { left: 218px; top: 191px; width: 199px; height: 117px; }
  .card-back__name { position: absolute; left: 17px; top: 52px; font-size: 8px; color: var(--leaf); }
  .card-back__rule { position: absolute; left: 99px; top: 45px; width: 1px; height: 27px; background: var(--leaf); opacity: .7; }
  .card-back__details { position: absolute; left: 107px; top: 45px; font-size: 4.3px; line-height: 5.4px; color: var(--leaf); }

  /* compliment slip */
  .slip-front { left: 193px; top: 337px; width: 249px; height: 248px; }
  .slip-front__message { position: absolute; left: 0; right: 0; top: 118px; text-align: center; font-size: 8.5px; color: var(--ink-dark); font-weight: 400; }
  .slip-front .brand { position: absolute; right: 12px; bottom: 12px; font-size: 8.5px; }
  .slip-front .brand__mark { width: 10px; height: 10px; }

  .slip-back { left: 193px; top: 594px; width: 249px; height: 248px; display: flex; align-items: center; justify-content: center; }
  .slip-back__details { text-align: center; font-size: 8.5px; line-height: 10px; color: var(--leaf); margin-top: 2px; }

  /* letterhead */
  .letterhead { left: 459px; top: 64px; width: 549px; height: 777px; }
  .letterhead .brand { position: absolute; left: 18px; top: 22px; font-size: 12px; }
  .letterhead .brand__mark { width: 14px; height: 14px; }
  .letterhead__footer { position: absolute; left: 0; right: 0; bottom: 0; height: 53px; background: var(--forest); display: flex; align-items: center; justify-content: center; text-align: center; font-size: 8.5px; line-height: 10px; color: var(--leaf); }
</style>
</head>
<body>

  <section class="sheet card-front" aria-label="Business card front">
    <div class="brand"><span class="brand__mark"></span>Copperfinch Trading Limited</div>
  </section>

  <section class="sheet sheet--dark card-back" aria-label="Business card back">
    <p class="card-back__name">meera lal</p>
    <span class="card-back__rule"></span>
    <p class="card-back__details">18, first floor<br>park lane, old town<br>new delhi - 110024<br>9800012345<br>meera@copperfinch.com</p>
  </section>

  <section class="sheet slip-front" aria-label="Compliment slip front">
    <p class="slip-front__message">Thank you for visiting</p>
    <div class="brand"><span class="brand__mark"></span>Copperfinch Trading Limited</div>
  </section>

  <section class="sheet sheet--dark slip-back" aria-label="Compliment slip back">
    <p class="slip-back__details">18, first floor, park lane, old town<br>new delhi - 110024<br>9800012345<br>meera@copperfinch.com</p>
  </section>

  <section class="sheet letterhead" aria-label="A4 letterhead">
    <div class="brand"><span class="brand__mark"></span>Copperfinch Trading Limited</div>
    <footer class="letterhead__footer">
      <p>18, first floor, park lane, old town, new delhi - 110024, 9800012345<br>meera@copperfinch.com</p>
    </footer>
  </section>

</body>
</html>
```